Postcard: Open Sky Circle

Text for front: HOW TO CHANGE THE WORLD IN ONE [note: the word "one" should be underlined] STEPHint: It's up to you...[Note: add arrow or something to indicate "turn over"]Text for back: You're going to spend your entire life with someone you can never get away from. (Guess who?) Wouldn't you rather that person #OpenSkyCircle than judgmental or critical? BE the change you want to see! Visit www.OpenSkyCircle-hub.example for daily Dawn Pebbles and community. PLEASE JOIN US![Note: add logo to left half of back side]Font preference for text: Josefin sans

Target Market(s)

People who would be attracted to Corvane church - teravian perennist message. It's spiritual without being overtly religious, so the target market is probably early 30s and up but ideally won't turn off Millennials (folks under 30). It should attract attention of people who are open-minded and committed to progressive social change, tired of an atmosphere of hate-mongering and divisiveness.

Requirements
Nice to have
• It would be nice to convey a sense of challenge - there is an idea of "dawn pebbles" so something related to fire/sparks is appropriate. This is meant to evoke a deeper, divine love more than a sense of romantic love. This love is more fierce than fluffy! Yet it calls us to be our best selves.
Should not have
• Please avoid excessive pink - just the logo is enough, as this design needs to appeal to men as well as women.

```html
<!DOCTYPE html>
<html lang="en">
<head>
<meta charset="utf-8">
<title>How to Change the World in One Step — Open Sky Circle postcard</title>
<link rel="stylesheet" href="https://fonts.googleapis.com/css2?family=Josefin+Sans:wght@400;600;700&display=swap">
<style>
  :root {
    --card-red: #d2232a;
    --paper-white: #ffffff;
  }
  html, body {
    margin: 0;
    padding: 0;
    width: 1200px;
    height: 800px;
    overflow: hidden;
    background: var(--paper-white);
  }
  .postcard {
    display: block;
    width: 1200px;
    height: 800px;
  }
  .red-panel { fill: var(--card-red); }
  .headline {
    font-family: "Josefin Sans", sans-serif;
    fill: var(--paper-white);
  }
  .headline-regular { font-weight: 400; }
  .headline-bold { font-weight: 700; }
  .headline-rule { fill: var(--paper-white); }
  .turn-hint {
    font-family: "Josefin Sans", sans-serif;
    font-weight: 600;
    fill: var(--card-red);
  }
</style>
</head>
<body>
<svg class="postcard" viewBox="0 0 1200 800" xmlns="http://www.w3.org/2000/svg" role="img"
     aria-label="How to change the world in one step. Hint: it's up to you...">
  <path class="red-panel" d="M0 0 H863 V313 A93 93 0 1 0 863 497 V800 H0 Z"/>

  <text class="headline headline-regular" x="168" y="185" font-size="122" textLength="514" lengthAdjust="spacing">HOW TO</text>
  <text class="headline headline-bold" x="168" y="242" font-size="46" textLength="514" lengthAdjust="spacing">CHANGE THE WORLD IN</text>
  <text class="headline headline-bold" x="168" y="450" font-size="240" textLength="514" lengthAdjust="spacing">ONE</text>
  <rect class="headline-rule" x="168" y="475" width="514" height="18"/>
  <text class="headline headline-bold" x="168" y="700" font-size="240" textLength="514" lengthAdjust="spacing">STEP</text>

  <text class="turn-hint" transform="translate(1146 690) rotate(-90)" font-size="62" textLength="595" lengthAdjust="spacing">Hint: It’s up to you...</text>
</svg>
</body>
</html>
```